Brusque Premium Men's Shaving Cream Product Label . Cream packaged in a Amber Jar/Black Top Cap.

Please include information ( see Brusque design Template attachment) designed on a Round Top cap. Label Diameter: 3.125" NOTE: Design this First,
Wrap Around Label: 11.3125 x 0.875" (w x h): NOTE: Required latter after selection of Final Design Selection.
Shave Cream packaged in an 8oz Low Profile Amber Jar/Black Top Cap.
Thanks

Target Market(s)

Prime Target-Men Ages 20yrs-65yrs+ and Women 20yrs-65yrs+( they purchase ovr 55% of these Mens care products for partner/spouse/friend.

Industry/Entity Type

Personel Care/Cosmetics/NaturalHealthcare

Other font styles liked:
• At this stage if you would like to submi a desigh that would include both a Top Label and your Wrap-around label on a Amber jar/black top lid. It would be helpful to see how it would look complete. Thanks . Please refer to the updated design Graphic Template for copy and layout . Questions? Let me know. Thanks.Please now use TIMBERLAND on label designs. Thanks! Please see image attachment for added Tree Image Vector that can be added to your design instead of the Original Tree Image .

Requirements
Must have
• Look and Feel of a Quality/Premium Mens Skincare Brand with a Masculine feel but attractive to women as well ( not Macho!).Think Unisex with a Male slant.
Nice to have
• Premium/Quality/Natural Skincare & Bodycare Brand
Should not have
• Not Macho. No Cartoony or Barber Tools/Bearded Men Images. Too gimicky and over-hyped!

```html
<!DOCTYPE html>
<html lang="en">
<head>
<meta charset="utf-8">
<title>Brusque Shaving Cream – Lid Label Options</title>
<link href="https://fonts.googleapis.com/css2?family=Alegreya:wght@400;500&family=Cinzel:wght@400;500&family=Montserrat:wght@400;500&family=Tenor+Sans&display=swap" rel="stylesheet">
<style>
  :root {
    --bg-option-one: #84703f;
    --bg-option-two: #908b66;
    --lid-black: #252324;
    --lid-rim: #1c1b1b;
    --gold: #a07f42;
    --gold-light: #c49a52;
    --gold-band: #9c7a3e;
    --ivory: #f4f1ea;
    --ink: #2b2a26;
  }
  * { margin: 0; padding: 0; box-sizing: border-box; }
  html, body { width: 1200px; height: 580px; overflow: hidden; }
  body { position: relative; font-family: "Montserrat", sans-serif; }
  .option { position: absolute; top: 0; height: 580px; }
  .option--one { left: 0; width: 599px; background: var(--bg-option-one); }
  .option--two { left: 599px; width: 601px; background: var(--bg-option-two); }
  .option svg { display: block; position: absolute; inset: 0; }
  .option-number {
    position: absolute; font-family: "Montserrat", sans-serif; font-weight: 400;
    font-size: 26px; color: var(--ink); line-height: 1;
  }
  .option--one .option-number { left: 34px; top: 526px; }
  .option--two .option-number { left: 42px; top: 536px; }
  .brand-name { font-family: "Montserrat", sans-serif; font-weight: 500; letter-spacing: 3px; }
  .serif-sans { font-family: "Tenor Sans", sans-serif; }
  .book-serif { font-family: "Alegreya", serif; }
  .roman-caps { font-family: "Cinzel", serif; }
</style>
</head>
<body>

<section class="option option--one">
  <svg width="599" height="580" viewBox="0 0 599 580">
    <defs>
      <clipPath id="lid-one-face"><circle cx="308" cy="268" r="180"/></clipPath>
      <radialGradient id="tree-tones-one" cx="50%" cy="45%" r="60%">
        <stop offset="0" stop-color="#c99f58"/>
        <stop offset="1" stop-color="#5b4527"/>
      </radialGradient>
    </defs>

    <circle class="lid-rim" cx="308" cy="268" r="184" fill="var(--lid-rim)"/>
    <circle class="lid-face" cx="308" cy="268" r="180" fill="var(--lid-black)"/>
    <circle class="inner-ring" cx="308" cy="268" r="172" fill="none" stroke="var(--gold)" stroke-width="0.6"/>

    <g class="weight-band" clip-path="url(#lid-one-face)">
      <rect x="100" y="408" width="420" height="60" fill="var(--gold-band)"/>
    </g>

    <g class="pinstripes" stroke="var(--gold)" stroke-width="0.7" clip-path="url(#lid-one-face)">
      <line x1="100" y1="231" x2="254" y2="231"/><line x1="361" y1="231" x2="520" y2="231"/>
      <line x1="100" y1="236.7" x2="254" y2="236.7"/><line x1="361" y1="236.7" x2="520" y2="236.7"/>
      <line x1="100" y1="242.4" x2="254" y2="242.4"/><line x1="361" y1="242.4" x2="520" y2="242.4"/>
      <line x1="100" y1="248.1" x2="254" y2="248.1"/><line x1="361" y1="248.1" x2="520" y2="248.1"/>
      <line x1="100" y1="253.8" x2="254" y2="253.8"/><line x1="361" y1="253.8" x2="520" y2="253.8"/>
      <line x1="100" y1="259.5" x2="254" y2="259.5"/><line x1="361" y1="259.5" x2="520" y2="259.5"/>
      <line x1="100" y1="265.2" x2="254" y2="265.2"/><line x1="361" y1="265.2" x2="520" y2="265.2"/>
      <line x1="100" y1="270.9" x2="254" y2="270.9"/><line x1="361" y1="270.9" x2="520" y2="270.9"/>
      <line x1="100" y1="276.6" x2="254" y2="276.6"/><line x1="361" y1="276.6" x2="520" y2="276.6"/>
    </g>

    <text class="brand-name" x="308" y="150" text-anchor="middle" font-size="17" fill="var(--ivory)">BRUSQUE</text>

    <text class="product-name serif-sans" x="308" y="198" text-anchor="middle" font-size="33" fill="var(--gold)" letter-spacing="0.5">FORESTMOOR</text>

    <circle class="tree-emblem" role="img" aria-label="Golden tree of life emblem with roots" cx="308" cy="256" r="49" fill="url(#tree-tones-one)"/>

    <text class="product-type book-serif" x="308" y="331" text-anchor="middle" font-size="21" fill="var(--ivory)" letter-spacing="2.2">SHAVING CREAM</text>
    <text class="product-type-fr book-serif" x="308" y="351" text-anchor="middle" font-size="14" fill="var(--ivory)" letter-spacing="1.8">CRÈME DE RASAGE</text>

    <g class="scent-line" stroke="var(--gold)" stroke-width="0.7">
      <line x1="174" y1="372" x2="230" y2="372"/>
      <line x1="386" y1="372" x2="442" y2="372"/>
      <line x1="264" y1="389" x2="284" y2="389"/>
      <line x1="332" y1="389" x2="352" y2="389"/>
    </g>
    <text class="scent-name book-serif" x="308" y="376" text-anchor="middle" font-size="13" fill="var(--gold)" letter-spacing="0.6">OAKHAVEN RESERVE</text>
    <text class="founded book-serif" x="308" y="394" text-anchor="middle" font-size="11" fill="var(--ivory)" letter-spacing="2.5">1935</text>

    <text class="net-weight book-serif" x="308" y="423" text-anchor="middle" font-size="10" fill="var(--ivory)">150g ℮ 5.3 oz</text>
  </svg>
  <span class="option-number">1</span>
</section>

<section class="option option--two">
  <svg width="601" height="580" viewBox="0 0 601 580">
    <defs>
      <path id="title-arc" d="M 230 287 A 70 70 0 1 1 362 287"/>
      <radialGradient id="tree-tones-two" cx="50%" cy="45%" r="60%">
        <stop offset="0" stop-color="#d0a65c"/>
        <stop offset="0.7" stop-color="#3a2e1c"/>
        <stop offset="1" stop-color="#111"/>
      </radialGradient>
    </defs>

    <circle class="lid-rim" cx="296" cy="274" r="183" fill="var(--gold-light)"/>
    <circle class="lid-face" cx="296" cy="274" r="179" fill="var(--lid-black)"/>
    <circle class="inner-ring" cx="296" cy="274" r="169" fill="none" stroke="var(--gold-light)" stroke-width="1"/>

    <text class="brand-name" x="296" y="157" text-anchor="middle" font-size="16" fill="var(--ivory)">BRUSQUE</text>

    <text class="product-name roman-caps" font-size="28" fill="var(--gold-light)">
      <textPath href="#title-arc" startOffset="50%" text-anchor="middle" textLength="250" lengthAdjust="spacing">FORESTMOOR</textPath>
    </text>

    <circle class="emblem-ground" cx="296" cy="262" r="52" fill="#111"/>
    <circle class="tree-emblem" role="img" aria-label="Golden tree of life emblem with roots" cx="296" cy="262" r="47" fill="url(#tree-tones-two)"/>

    <path class="title-frame" d="M 134 315 L 175 315 Q 177 315 177 320 L 177 358 Q 177 365 186 365 L 406 365 Q 415 365 415 358 L 415 320 Q 415 315 420 315 L 458 315" fill="none" stroke="var(--gold-light)" stroke-width="0.9"/>

    <text class="product-type" x="296" y="336" text-anchor="middle" font-size="16" font-weight="500" fill="var(--ivory)" letter-spacing="2.6">SHAVING CREAM</text>
    <text class="product-type-fr" x="296" y="357" text-anchor="middle" font-size="11" fill="var(--ivory)" letter-spacing="2.2">CRÈME DE RASAGE</text>

    <text class="scent-name" x="296" y="385" text-anchor="middle" font-size="10.5" font-weight="500" fill="var(--gold-light)" letter-spacing="2.6">OAKHAVEN RESERVE</text>
    <g class="founded-rules" stroke="var(--ivory)" stroke-width="0.6">
      <line x1="261" y1="397.5" x2="278" y2="397.5"/>
      <line x1="314" y1="397.5" x2="331" y2="397.5"/>
    </g>
    <text class="founded" x="296" y="401" text-anchor="middle" font-size="9" fill="var(--ivory)" letter-spacing="2">1935</text>

    <text class="net-weight" x="296" y="424" text-anchor="middle" font-size="8.5" fill="var(--ivory)">150g ℮ 5.3 oz</text>
  </svg>
  <span class="option-number">2</span>
</section>

</body>
</html>
```